JT Holly Cleaning Business Card

We need a business card for our new business, a cleaning company using steam. We already have a logo, and would like a modern-looking card using colors that go well with those in our logo.

```html
<!DOCTYPE html>
<html lang="en">
<head>
<meta charset="utf-8">
<title>JT Holly Cleaning Business Card</title>
<link rel="stylesheet" href="https://fonts.googleapis.com/css2?family=Open+Sans:wght@400;600;700&display=swap">
<style>
  :root {
    --bg: #2b2b2b;
    --card: #f7f7f7;
    --blue: #1a6fd6;
    --green: #5cbf1f;
    --ink: #222;
    --muted: #8a8a8a;
    --dark-band: #1e1e1e;
  }
  html, body {
    margin: 0;
    width: 1200px;
    height: 997px;
    overflow: hidden;
    background: var(--bg);
    font-family: "Open Sans", Arial, sans-serif;
  }
  .card {
    position: absolute;
    left: 250px;
    width: 700px;
    height: 400px;
    background: var(--card);
    overflow: hidden;
    box-shadow: 0 10px 30px rgba(0,0,0,.5);
  }
  .card--front { top: 70px; }
  .card--back { top: 527px; }
  .card__edge {
    position: absolute;
    left: 0; top: 0;
    width: 700px; height: 400px;
  }
  .brand {
    position: absolute;
    display: flex;
    align-items: center;
    gap: 16px;
  }
  .brand__dot {
    width: 74px; height: 74px;
    border-radius: 50%;
    background: var(--green);
    flex: none;
  }
  .brand__name {
    font-weight: 700;
    font-size: 40px;
    color: var(--blue);
    line-height: 1;
    white-space: nowrap;
  }
  .card--front .brand { left: 110px; top: 150px; }
  .website {
    position: absolute;
    left: 330px; top: 300px;
    font-size: 15px;
    font-weight: 600;
    color: var(--blue);
  }
  .card--back .brand { left: 180px; top: 56px; }
  .card--back .brand__dot { width: 62px; height: 62px; }
  .card--back .brand__name { font-size: 34px; }
  .person {
    position: absolute;
    right: 60px; top: 172px;
    text-align: left;
  }
  .person__name {
    font-weight: 700;
    font-size: 20px;
    color: var(--blue);
  }
  .person__role {
    font-size: 12px;
    letter-spacing: .5px;
    color: var(--muted);
    text-transform: uppercase;
  }
  .contact-tab {
    position: absolute;
    left: 0; top: 206px;
    width: 40px; height: 158px;
    background: var(--blue);
    border-radius: 0 10px 10px 0;
    display: flex;
    flex-direction: column;
    justify-content: space-around;
    align-items: center;
    padding: 8px 0;
    box-sizing: border-box;
  }
  .contact-tab svg { width: 18px; height: 18px; fill: #fff; }
  .contact-list {
    position: absolute;
    left: 60px; top: 212px;
    margin: 0; padding: 0;
    list-style: none;
    font-size: 14px;
    color: var(--ink);
  }
  .contact-list li { height: 36px; line-height: 36px; white-space: nowrap; }
</style>
</head>
<body>

<section class="card card--front">
  <svg class="card__edge" viewBox="0 0 700 400" aria-hidden="true">
    <path d="M0 372 L700 372 L700 400 L0 400 Z" fill="var(--dark-band)"/>
    <path d="M500 372 Q512 338 548 338 L700 338 L700 372 Z" fill="var(--blue)"/>
  </svg>
  <div class="brand">
    <span class="brand__dot"></span>
    <span class="brand__name">JT Holly Cleaning</span>
  </div>
  <div class="website">www.jthollycleaning.com</div>
</section>

<section class="card card--back">
  <svg class="card__edge" viewBox="0 0 700 400" aria-hidden="true">
    <path d="M0 372 L700 372 L700 400 L0 400 Z" fill="var(--dark-band)"/>
    <path d="M500 372 Q512 338 548 338 L700 338 L700 372 Z" fill="var(--blue)"/>
  </svg>
  <div class="brand">
    <span class="brand__dot"></span>
    <span class="brand__name">JT Holly Cleaning</span>
  </div>
  <div class="person">
    <div class="person__name">Daniel Brooks</div>
    <div class="person__role">Marketing Strategist</div>
  </div>
  <div class="contact-tab">
    <svg viewBox="0 0 24 24" aria-label="Phone"><path d="M6.6 10.8a15 15 0 0 0 6.6 6.6l2.2-2.2c.3-.3.7-.4 1-.2 1.1.4 2.3.6 3.6.6.6 0 1 .4 1 1V20c0 .6-.4 1-1 1A17 17 0 0 1 3 4c0-.6.4-1 1-1h3.5c.6 0 1 .4 1 1 0 1.3.2 2.5.6 3.6.1.3 0 .7-.2 1z"/></svg>
    <svg viewBox="0 0 24 24" aria-label="Fax"><path d="M6 2h10l2 2v5H6zM4 10h16a2 2 0 0 1 2 2v6h-4v4H6v-4H2v-6a2 2 0 0 1 2-2zm4 6v4h8v-4z"/></svg>
    <svg viewBox="0 0 24 24" aria-label="Email"><path d="M2 5h20v14H2zm2 2v.5l8 5 8-5V7l-8 5z"/></svg>
    <svg viewBox="0 0 24 24" aria-label="Address"><path d="M12 2a7 7 0 0 0-7 7c0 5 7 13 7 13s7-8 7-13a7 7 0 0 0-7-7zm0 9.5A2.5 2.5 0 1 1 12 6.5a2.5 2.5 0 0 1 0 5z"/></svg>
  </div>
  <ul class="contact-list">
    <li>214-555-0148</li>
    <li>267-555-0192</li>
    <li>hello@jthollycleaning.com</li>
    <li>42 Cedar Lane, Plano TX 75024</li>
  </ul>
</section>

</body>
</html>
```